Letterhead for small civil engineer company

We need bold and modern design for company letterhead in MS word. It needs to have company logo and company info. Somewhere in the upper right part of document needs to be space for "recever" and the documents starts with, example, "SUBJECT: CIVIL ENGINEER LETTERHEAD".

in the bottom part of document needs to be signature and date.

Company info: Veltrana d.o.o., Lipovac 15, Lipovac (Općina Brdarić), OIB 47396028154, www.veltrana.hr, info@veltrana.hr

Email of document sender needs to be somewhere if document, exapmle xyz@veltrana.hr

Target Market(s)

Civil engineer company and projects

Industry/Entity Type

Civil engineer

Font styles to use
Serif

Colors
F0912C
F2A743
F7CA91
FBE8D2
FDF5EE

Requirements
Must have
• Company logo and company info
Nice to have
• Moder and clean design
Should not have
• Too much details

```html
<!DOCTYPE html>
<html lang="hr">
<head>
<meta charset="utf-8">
<title>Veltrana d.o.o. – Letterhead</title>
<link href="https://fonts.googleapis.com/css2?family=Space+Grotesk:wght@400;500;700&display=swap" rel="stylesheet">
<style>
  :root {
    --backdrop: #b3b3b3;
    --paper: #ffffff;
    --brand-orange: #ec7d22;
    --footer-grey: #666666;
    --ink: #1c1c1c;
    --rule: #8a8a8a;
    --muted: #6e6e6e;
  }
  * { margin: 0; padding: 0; box-sizing: border-box; }
  html, body { width: 1200px; height: 1000px; overflow: hidden; }
  body {
    background: var(--backdrop);
    font-family: "Space Grotesk", sans-serif;
    position: relative;
  }
  .letterhead {
    position: absolute;
    left: 297px; top: 72px;
    width: 606px; height: 855px;
    background: var(--paper);
    box-shadow: 0 2px 6px rgba(0,0,0,0.18);
    overflow: hidden;
  }
  .brand {
    position: absolute; left: 26px; top: 28px;
    display: flex; align-items: center; gap: 12px;
  }
  .brand-square {
    width: 34px; height: 34px;
    border: 1.5px solid var(--footer-grey);
  }
  .brand-name {
    color: var(--brand-orange);
    font-size: 24px; font-weight: 500; letter-spacing: 0.5px;
  }
  .receiver {
    position: absolute; right: 38px; top: 45px;
    font-size: 11px; color: var(--ink);
  }
  .sender {
    position: absolute; left: 30px; top: 104px;
    font-size: 11px; line-height: 14px; color: var(--ink);
  }
  .subject {
    position: absolute; left: 30px; top: 145px;
    font-size: 11px; line-height: 15px; color: var(--ink);
  }
  .subject-label { font-weight: 700; }
  .sign-field {
    position: absolute; top: 694px;
    width: 160px; height: 40px;
    text-align: center;
  }
  .sign-field .line {
    height: 1px; background: var(--rule); margin-top: 19px;
  }
  .sign-field .caption {
    font-size: 8px; color: var(--muted); margin-top: 5px;
  }
  .signature { left: 225px; }
  .date { left: 418px; }
  .date-slashes {
    position: absolute; top: 6px; left: 0; width: 100%;
    font-size: 9px; color: var(--ink);
  }
  .date-slashes span { position: absolute; }
  .footer {
    position: absolute; left: 0; bottom: 0;
    width: 100%; height: 81px;
    background: var(--footer-grey);
    border-bottom: 3px solid var(--brand-orange);
    color: #ffffff; font-size: 11.5px; line-height: 15px;
  }
  .footer-company {
    position: absolute; left: 41px; top: 30px; font-weight: 700;
  }
  .footer-address {
    position: absolute; right: 227px; top: 15px; text-align: right;
  }
  .footer-contact {
    position: absolute; right: 38px; top: 30px; text-align: right;
  }
  .web-name { color: var(--brand-orange); font-weight: 700; }
</style>
</head>
<body>
  <main class="letterhead">
    <header class="brand">
      <div class="brand-square"></div>
      <span class="brand-name">VELTRANA</span>
    </header>

    <div class="receiver">recever</div>

    <div class="sender">
      <div>sender</div>
      <div>xyz@veltrana.hr</div>
    </div>

    <div class="subject">
      <div class="subject-label">SUBJECT:</div>
      <div>CIVIL ENGINEER LETTERHEAD</div>
    </div>

    <div class="sign-field signature">
      <div class="line"></div>
      <div class="caption">Signature</div>
    </div>

    <div class="sign-field date">
      <div class="date-slashes"><span style="left:57px">/</span><span style="left:98px">/</span></div>
      <div class="line"></div>
      <div class="caption">Date</div>
    </div>

    <footer class="footer">
      <div class="footer-company">VELTRANA D.O.O.</div>
      <div class="footer-address">
        <div>LIPOVAC 15</div>
        <div>LIPOVAC (OPĆINA BRDARIĆ)</div>
        <div>OIB 47396028154</div>
      </div>
      <div class="footer-contact">
        <div>info@veltrana.hr</div>
        <div><span class="web-name">veltrana</span>.hr</div>
      </div>
    </footer>
  </main>
</body>
</html>
```